Magnetic Business card Design do a service provider

Hi,

The company aim is to provide all service needs under one roof. However, at the moment there is only Accounting, Electrical and IT branches. There will be more services coming onboard in the future.

I already have a logo designed (Company name is already part of the logo), I now need a magnetic business card designed.

The business card will contain the following:

- Company Logo
- Contact#
- E-mail
- enough space to add website URL (for future)
Updates

Project Deadline Extended Reason: HI All,The deadline has been extended due to not having enough time to review an overwhelming number of designs that has been submitted by lots of designers.I will be uploading a draft of designs that i have in mind.Thanks. Added Friday, January 22, 2016

Target Market(s)

Residential, Home-based Businesses, Small and Medium businesses

Industry/Entity Type

Business

Contact Information for Business Card

Contact#: 0491 738 552
E-mail: service@brightharborgroup.net.au

Font styles to use
Decorative
Script

Requirements
Must have
• Round edges
• Some form of logo incorporation as a background

```html
<!DOCTYPE html>
<html lang="en">
<head>
<meta charset="utf-8">
<title>Bright Harbor Group – Business Card</title>
<link href="https://fonts.googleapis.com/css2?family=Fondamento:ital@0;1&family=Cinzel:wght@500&display=swap" rel="stylesheet">
<style>
  :root {
    --page: #e9ecef;
    --card-blue: #33aedb;
    --card-grey: #a9adb1;
    --grey-edge: #c3c6c9;
    --ink-light: #ffffff;
    --ink-brand: #1d5fa8;
    --ink-dark: #2a2c2f;
  }
  * { margin: 0; padding: 0; box-sizing: border-box; }
  html, body { width: 1200px; height: 800px; overflow: hidden; }
  body {
    background: var(--page);
    display: flex; align-items: center; justify-content: center;
  }
  .card {
    position: relative;
    width: 1000px; height: 600px;
    border-radius: 44px;
    overflow: hidden;
    background: var(--card-blue);
    box-shadow: 0 18px 40px rgba(0,0,0,.18);
  }
  .card__backdrop { position: absolute; inset: 0; }
  .brand {
    position: absolute; left: 70px; top: 240px;
    display: flex; align-items: center; gap: 22px;
  }
  .brand__dot {
    width: 70px; height: 70px; border-radius: 50%;
    background: var(--ink-brand);
  }
  .brand__name {
    font-family: "Fondamento", cursive;
    font-size: 46px; line-height: 1.05;
    color: var(--ink-brand);
  }
  .contact {
    position: absolute; right: 70px; top: 90px;
    text-align: right;
    color: var(--ink-light);
  }
  .contact__name {
    font-family: "Cinzel", serif;
    font-size: 40px; font-style: italic; letter-spacing: 2px;
    margin-right: 52px;
  }
  .contact__role {
    font-family: "Cinzel", serif;
    font-size: 16px; letter-spacing: 2px;
    margin-right: 240px; margin-bottom: 34px;
  }
  .contact__list { list-style: none; }
  .contact__item {
    display: flex; align-items: center; justify-content: flex-end; gap: 16px;
    font-family: "Fondamento", cursive; font-style: italic;
    font-size: 27px; line-height: 1; margin-bottom: 16px;
  }
  .contact__item--plain { margin-right: 52px; }
  .icon {
    width: 36px; height: 36px; border-radius: 50%;
    background: var(--ink-light);
    display: flex; align-items: center; justify-content: center;
    flex: none;
  }
  .icon svg { width: 20px; height: 20px; }
</style>
</head>
<body>
  <div class="card">
    <svg class="card__backdrop" viewBox="0 0 1000 600" aria-hidden="true">
      <circle cx="170" cy="180" r="470" fill="var(--grey-edge)"/>
      <circle cx="170" cy="180" r="462" fill="var(--card-grey)"/>
    </svg>

    <div class="brand">
      <span class="brand__dot"></span>
      <span class="brand__name">Bright Harbor<br>Group</span>
    </div>

    <div class="contact">
      <p class="contact__name">Your Name</p>
      <p class="contact__role">Place</p>
      <ul class="contact__list">
        <li class="contact__item">Address Line 1, 201455
          <span class="icon"><svg viewBox="0 0 24 24"><path fill="#33aedb" d="M12 2a7 7 0 0 0-7 7c0 5 7 13 7 13s7-8 7-13a7 7 0 0 0-7-7zm0 9.5A2.5 2.5 0 1 1 12 6.5a2.5 2.5 0 0 1 0 5z"/></svg></span>
        </li>
        <li class="contact__item contact__item--plain">Address Line 2, EDF 2560</li>
        <li class="contact__item">0491 738 552
          <span class="icon"><svg viewBox="0 0 24 24"><path fill="#33aedb" d="M6.6 10.8a15 15 0 0 0 6.6 6.6l2.2-2.2a1 1 0 0 1 1-.25 11.4 11.4 0 0 0 3.6.57 1 1 0 0 1 1 1V20a1 1 0 0 1-1 1A17 17 0 0 1 3 4a1 1 0 0 1 1-1h3.5a1 1 0 0 1 1 1c0 1.25.2 2.45.57 3.6a1 1 0 0 1-.25 1z"/></svg></span>
        </li>
        <li class="contact__item">service@brightharborgroup.net.au
          <span class="icon"><svg viewBox="0 0 24 24"><path fill="#33aedb" d="M3 5h18v14H3zm2 2v.5l7 5 7-5V7l-7 5z"/></svg></span>
        </li>
        <li class="contact__item">www.brightharborgroup.net
          <span class="icon"><svg viewBox="0 0 24 24"><g fill="none" stroke="#33aedb" stroke-width="2"><circle cx="12" cy="12" r="9"/><path d="M3 12h18M12 3c3 3 3 15 0 18M12 3c-3 3-3 15 0 18"/></g></svg></span>
        </li>
      </ul>
    </div>
  </div>
</body>
</html>
```